Klenvo Disinfecting company

Company name: Klenvo Inc
We are starting up a new company that is a professional spray disinfecting company. We will be offering a service where we go into facilities like residential, office, child care, medical, dental, restaurant, entertainment, hotel/motel, automotive fleets with professional spraying equipment and disinfect their facilities for a fee. Our products kills a wide range of viruses and pathogens including Covid 19.

Target Market(s)

Residential, commercial office space, child care, medical, dental, restaurant, entertainment facilities, hotel/motel, automotive fleets.

Font styles to use
Sans Serif

Colors
31b7a3

Requirements
Must have
• Company name - Klenvo Inc
Phone - 905-487-2963
Email - klenvotrue@mailbox-example.com
Our Slogan - Disinfect Today For A Safe Tomorrow
Brief description of our reservice
Nice to have
• Some kind of a picture of a man with a sprayer, perhaps in a white coveralls, perhaps on a background of a few of the facilities in mention in my target market section. I have uploaded 4 examples of print ads form similar companies. I don't necessarily want them to look alike however these are very professional ads and will give you the gist of what I'm looking for.

```html
<!DOCTYPE html>
<html lang="en">
<head>
<meta charset="utf-8">
<title>Klenvo Inc — Disinfect Today For A Safe Tomorrow</title>
<link rel="stylesheet" href="https://fonts.googleapis.com/css2?family=Oswald:wght@500;700&family=Roboto:wght@400;500;700;900&family=Lato:wght@400;700;900&display=swap">
<style>
  :root {
    --page-bg: #d9d9d9;
    --paper: #ffffff;
    --brand-cyan: #22b6e3;
    --strip-cyan: #9adcee;
    --brand-green: #0b7a3a;
    --icon-green: #17a24a;
    --navy: #0d3a4c;
    --ink: #14232d;
    --band-grey: #ebebeb;
    --photo-warm: #8b6a4a;
    --photo-grey: #6f6f6f;
    --photo-light: #d8d2c8;
  }
  * { margin: 0; padding: 0; box-sizing: border-box; }
  html, body { width: 1200px; height: 1200px; overflow: hidden; background: var(--page-bg); }
  .flyer {
    position: absolute; left: 210px; top: 50px; width: 780px; height: 1100px;
    background: var(--paper); overflow: hidden;
    font-family: "Roboto", Arial, sans-serif; color: var(--ink);
  }
  .flyer-shapes { position: absolute; inset: 0; }
  .brand-name {
    position: absolute; left: 50px; top: 150px;
    font: 700 34px "Roboto", Arial, sans-serif; color: var(--brand-cyan); letter-spacing: 0.5px;
  }
  .slogan-banner {
    position: absolute; left: 50px; top: 215px; width: 460px; height: 210px;
    background: var(--brand-green); padding: 18px 26px; color: #fff;
  }
  .slogan-main { font: 700 96px/1 "Oswald", Impact, sans-serif; letter-spacing: 1px; }
  .slogan-sub { font: 500 40px/1.05 "Oswald", Arial, sans-serif; margin-top: 4px; }
  .slogan-sub strong { font-weight: 700; display: block; }
  .process-band {
    position: absolute; left: 0; top: 425px; width: 500px; height: 135px;
    background: var(--band-grey); padding: 30px 0 0 86px;
  }
  .process-title { font: 900 26px "Lato", Arial, sans-serif; }
  .process-text { font: 700 21px/1.2 "Lato", Arial, sans-serif; }
  .service-list { position: absolute; left: 50px; top: 590px; list-style: none; }
  .service-item { display: flex; align-items: center; height: 51px; }
  .service-icon {
    width: 40px; height: 40px; border-radius: 50%; background: var(--icon-green);
    box-shadow: 0 0 0 3px #fff, 0 0 0 5px var(--icon-green);
    display: flex; align-items: center; justify-content: center; margin-right: 22px;
  }
  .service-label { font: 700 26px "Oswald", Arial, sans-serif; color: var(--ink); letter-spacing: -0.3px; }
  .contact-block {
    position: absolute; right: 30px; top: 710px; width: 330px; text-align: right; color: #fff;
  }
  .contact-intro { font: 400 17px/1.3 "Roboto", Arial, sans-serif; }
  .contact-heading { font: 900 26px "Roboto", Arial, sans-serif; color: var(--ink); margin-top: 14px; }
  .contact-line { display: flex; justify-content: flex-end; align-items: center; gap: 12px; }
  .contact-phone { font: 500 40px "Roboto", Arial, sans-serif; margin-top: 4px; }
  .contact-email { font: 500 14px "Roboto", Arial, sans-serif; color: var(--ink); margin-top: 6px; }
  .contact-note { font: 500 15px/1.25 "Roboto", Arial, sans-serif; color: var(--ink); margin-top: 8px; }
  .contact-dot {
    width: 18px; height: 18px; border-radius: 50%; background: #fff; flex: none;
    display: flex; align-items: center; justify-content: center;
  }
</style>
</head>
<body>
<main class="flyer">
  <svg class="flyer-shapes" width="780" height="1100" viewBox="0 0 780 1100">
    <defs>
      <linearGradient id="photo-tone" x1="0" y1="0" x2="0" y2="1">
        <stop offset="0" stop-color="var(--photo-light)"/>
        <stop offset="0.45" stop-color="var(--photo-grey)"/>
        <stop offset="1" stop-color="var(--photo-warm)"/>
      </linearGradient>
    </defs>
    <circle cx="640" cy="230" r="412" fill="none" stroke="var(--brand-cyan)" stroke-width="4"/>
    <circle cx="640" cy="230" r="400" fill="url(#photo-tone)" role="img"
      aria-label="Photo: technician in white protective coveralls, respirator and yellow gloves holding a pump sprayer in an office meeting room"/>
    <circle cx="1100" cy="1150" r="780" fill="var(--navy)"/>
    <circle cx="1100" cy="1150" r="760" fill="var(--brand-cyan)"/>
    <rect x="0" y="1078" width="330" height="22" fill="var(--strip-cyan)"/>
  </svg>

  <div class="brand-name">KLENVO INC</div>

  <div class="slogan-banner">
    <div class="slogan-main">DISINFECT</div>
    <div class="slogan-sub">TODAY FOR A <strong>SAFE TOMORROW</strong></div>
  </div>

  <div class="process-band">
    <div class="process-title">OUR PROCESS</div>
    <div class="process-text">kills a wide range of<br>viruses including Covid 19.</div>
  </div>

  <ul class="service-list">
    <li class="service-item"><span class="service-icon"><svg width="20" height="20" viewBox="0 0 20 20"><path d="M2 10 10 3l8 7h-3v7H5v-7z" fill="#fff"/></svg></span><span class="service-label">Residential</span></li>
    <li class="service-item"><span class="service-icon"><svg width="20" height="20" viewBox="0 0 20 20"><rect x="5" y="2" width="10" height="16" fill="none" stroke="#fff" stroke-width="2"/><path d="M8 6h4M8 10h4M8 14h4" stroke="#fff" stroke-width="1.6"/></svg></span><span class="service-label">Commercial office space</span></li>
    <li class="service-item"><span class="service-icon"><svg width="22" height="20" viewBox="0 0 22 20"><path d="M3 12l3-6h10l3 6v4H3z" fill="#fff"/><circle cx="7" cy="16" r="2" fill="var(--icon-green)"/><circle cx="15" cy="16" r="2" fill="var(--icon-green)"/></svg></span><span class="service-label">Automotive fleets</span></li>
    <li class="service-item"><span class="service-icon"><svg width="20" height="20" viewBox="0 0 20 20"><rect x="4" y="3" width="12" height="15" fill="none" stroke="#fff" stroke-width="2"/><path d="M7 7h2M11 7h2M7 11h2M11 11h2" stroke="#fff" stroke-width="1.6"/></svg></span><span class="service-label">Hotel/motel</span></li>
    <li class="service-item"><span class="service-icon"><svg width="20" height="20" viewBox="0 0 20 20"><rect x="2" y="4" width="16" height="10" fill="none" stroke="#fff" stroke-width="2"/><path d="M7 17h6" stroke="#fff" stroke-width="2"/></svg></span><span class="service-label">Entertainment facilities</span></li>
    <li class="service-item"><span class="service-icon"><svg width="20" height="20" viewBox="0 0 20 20"><rect x="4" y="3" width="12" height="15" fill="none" stroke="#fff" stroke-width="2"/><path d="M7 7h6M7 11h6M7 15h6" stroke="#fff" stroke-width="1.6"/></svg></span><span class="service-label">Restaurant</span></li>
    <li class="service-item"><span class="service-icon"><svg width="20" height="20" viewBox="0 0 20 20"><path d="M4 5c0-3 5-2 6-1 1-1 6-2 6 1 0 4-2 5-2 11-2 0-2-5-4-5s-2 5-4 5c0-6-2-7-2-11z" fill="#fff"/></svg></span><span class="service-label">Dental</span></li>
    <li class="service-item"><span class="service-icon"><svg width="20" height="20" viewBox="0 0 20 20"><path d="M5 3v5a4 4 0 0 0 8 0V3M9 12v3a3 3 0 0 0 6 0v-3" fill="none" stroke="#fff" stroke-width="1.8"/><circle cx="15" cy="11" r="1.6" fill="#fff"/></svg></span><span class="service-label">Medical</span></li>
    <li class="service-item"><span class="service-icon"><svg width="20" height="20" viewBox="0 0 20 20"><path d="M6 18V8M9 18V4M12 18V5M15 18V8" stroke="#fff" stroke-width="2.4" stroke-linecap="round"/></svg></span><span class="service-label">Child care</span></li>
  </ul>

  <div class="contact-block">
    <p class="contact-intro">At Klenvo we are<br>dedicated to the cleanliness and<br>hygiene of our customers facilities.</p>
    <p class="contact-heading">CONTACT US TODAY</p>
    <p class="contact-line contact-phone">905-487-2963 <span class="contact-dot"><svg width="10" height="10" viewBox="0 0 10 10"><path d="M2 1l2 2-1 1c1 1 2 2 3 3l1-1 2 2-1 1C5 9 1 5 1 2z" fill="var(--navy)"/></svg></span></p>
    <p class="contact-line contact-email">klenvotrue@mailbox-example.com <span class="contact-dot"><svg width="10" height="10" viewBox="0 0 10 10"><rect x="1" y="2.5" width="8" height="5.5" fill="var(--navy)"/><path d="M1 2.5l4 3 4-3" stroke="#fff" fill="none"/></svg></span></p>
    <p class="contact-line contact-note">Lorem Ipsum is simply dummy text of<br>the printing and <span class="contact-dot"><svg width="10" height="10" viewBox="0 0 10 10"><path d="M5 9C3 6 2 5 2 4a3 3 0 0 1 6 0c0 1-1 2-3 5z" fill="var(--navy)"/></svg></span></p>
  </div>
</main>
</body>
</html>
```